Flyer overhaul from current flyers

I need to have our current flyers updated with a fresher look. We also need to have a new utility and real estate flyer created that will go along with the design of the new flyer. We are looking for new pictures, new overall design, same color scheme but would like to have the flyers more airy and inviting.

Target Market(s)

decision makers in the healthcare/utilty/banking/real estate sectors

Font styles to use
Other font styles liked:
• Logo is in Bell MT

Colors
0054AA
0677BA
7BADD7
CADEEF
E8F1F8

Requirements
Must have
• Close to what is currently on the existing flyers

```html
<!DOCTYPE html>
<html lang="en">
<head>
<meta charset="utf-8">
<title>Tri-River Recovery Flyers</title>
<link href="https://fonts.googleapis.com/css2?family=Libre+Caslon+Text:wght@400;700&family=Montserrat:wght@400;500;600&display=swap" rel="stylesheet">
<style>
:root{
  --board:#e6e7e8;
  --sky:#00aee6;
  --blue:#0677ba;
  --deep:#0054aa;
  --navy:#0b4a72;
  --ink:#083a5c;
  --pale:#7badd7;
  --mist:#cadeef;
  --frost:#e8f1f8;
  --slate:#3d4449;
  --white:#ffffff;
  --serif:"Libre Caslon Text", Georgia, serif;
  --sans:"Montserrat", Arial, sans-serif;
}
*{box-sizing:border-box;margin:0;padding:0}
html,body{width:844px;height:1200px;overflow:hidden;background:var(--board)}
.board{position:relative;width:844px;height:1200px}
.slot{position:absolute;width:381.5px;height:494px;box-shadow:0 3px 8px rgba(0,0,0,.22);overflow:hidden}
.slot-tl{left:19px;top:52px}
.slot-tr{left:437px;top:52px}
.slot-bl{left:19.5px;top:574.5px}
.slot-br{left:437px;top:574.5px}
.flyer{position:absolute;left:0;top:0;width:664px;height:860px;transform:scale(.5745);transform-origin:0 0;overflow:hidden;font-family:var(--sans);color:var(--white)}
.flyer-services{background:linear-gradient(180deg,var(--sky) 0%,#0a86c0 30%,var(--navy) 75%,#0a4268 100%)}
.flyer-philosophy{background:var(--white)}
.shapes{position:absolute;left:0;top:0;width:664px;height:860px}
.brand{position:absolute;left:36px;top:40px;display:flex;align-items:center;gap:14px}
.brand-dot{width:82px;height:82px;border-radius:50%;border:6px solid var(--white)}
.brand-name{font-family:var(--serif);font-weight:400;font-size:29px;line-height:27px;color:var(--white);letter-spacing:.5px}
.title{position:absolute;left:36px;font-family:var(--serif);font-weight:700;white-space:nowrap}
.title-main{display:block;font-size:44px;line-height:50px;letter-spacing:.5px}
.title-sub{display:block;font-size:34px;line-height:40px;letter-spacing:.5px}
.tagline{position:absolute;left:36px;font-family:var(--serif);font-size:21px;line-height:29px;color:var(--pale)}
.features{position:absolute;left:34px;list-style:none}
.features li{display:flex;align-items:center;gap:12px;font-size:13.5px;font-weight:500;line-height:16px;height:55px;white-space:nowrap}
.features svg{width:34px;height:34px;flex:none}
.bundle{position:absolute;left:37px;top:633px;width:627px;height:135px;border-radius:68px 0 0 0;background:linear-gradient(90deg,var(--sky) 0%,#0886c4 35%,#0b5a8a 100%)}
.bundle-title{position:absolute;left:27px;top:26px;font-family:var(--serif);font-size:21px;line-height:29px}
.bundle-list{position:absolute;top:30px;list-style:none;font-size:11.5px;line-height:18px;color:var(--frost);white-space:nowrap}
.bundle-list li::before{content:"";display:inline-block;width:4px;height:4px;border-radius:50%;background:var(--white);margin-right:4px;vertical-align:middle}
.call{position:absolute;left:37px;width:292px;height:64px;background:var(--white);border-radius:0 32px 32px 32px;color:var(--deep);padding:6px 0 0 26px}
.call-label{font-size:14px;font-weight:600;color:var(--ink);line-height:16px}
.call-number{display:flex;align-items:center;gap:4px;font-size:29px;font-weight:600;line-height:34px}
.call-number svg{width:24px;height:24px}
.web{position:absolute;left:338px;width:294px;height:38px;border-bottom:2px solid var(--pale);display:flex;align-items:center;gap:8px;font-family:var(--serif);font-size:16px;font-weight:700;white-space:nowrap}
.web svg{width:16px;height:16px}
.philosophy-head{position:absolute;left:37px;top:562px;display:flex;align-items:flex-end;width:590px}
.philosophy-head h2{font-family:var(--serif);font-weight:700;font-size:36px;line-height:40px;letter-spacing:.5px;white-space:nowrap}
.philosophy-head span{flex:1;height:2px;background:var(--sky);margin:0 0 6px 4px}
.philosophy-copy{position:absolute;left:37px;top:614px;width:592px;font-size:11.6px;line-height:18px;color:var(--frost)}
.flyer-philosophy .web{left:330px;width:300px}
</style>
</head>
<body>
<main class="board">

  <section class="slot slot-tl">
    <div class="flyer flyer-services">
      <svg class="shapes" viewBox="0 0 664 860">
        <defs>
          <radialGradient id="finPhoto" cx=".55" cy=".45" r=".6">
            <stop offset="0" stop-color="#3b56c8"/>
            <stop offset=".6" stop-color="#2a3a9a"/>
            <stop offset="1" stop-color="#4d3d7c"/>
          </radialGradient>
        </defs>
        <path d="M664 30 C500 40 370 140 330 250 C295 340 280 420 290 480 C320 600 460 670 664 665 Z" fill="#0a5f92" opacity=".8"/>
        <path d="M664 50 C520 60 410 140 362 240 C322 320 302 380 304 430 C307 540 402 640 530 650 C590 654 635 648 664 642 Z" fill="var(--white)"/>
        <circle cx="602" cy="388" r="236" fill="url(#finPhoto)" role="img" aria-label="Photo of an open hand holding stacks of coins with a rising growth arrow and city skyline"/>
      </svg>
      <div class="brand"><span class="brand-dot"></span><span class="brand-name">TRI-RIVER<br>RECOVERY</span></div>
      <h1 class="title" style="top:180px"><span class="title-main">FINANCIAL</span><span class="title-sub">COLLECTIONS</span></h1>
      <p class="tagline" style="top:294px">A Forward<br>Thinking Approach</p>
      <ul class="features" style="top:355px">
        <li><svg viewBox="0 0 34 34" fill="none" stroke="#fff" stroke-width="1.6"><circle cx="17" cy="13" r="8"/><path d="M6 32c1-7 6-10 11-10s10 3 11 10"/></svg>Consumer Friendly,<br>Professional Approach</li>
        <li><svg viewBox="0 0 34 34" fill="none" stroke="#fff" stroke-width="1.6"><rect x="3" y="7" width="28" height="20"/><path d="M9 21l6-6 4 4 7-7"/></svg>Online Consumer Debt<br>Negotiation Tools</li>
        <li><svg viewBox="0 0 34 34" fill="none" stroke="#fff" stroke-width="1.6"><circle cx="12" cy="12" r="6"/><path d="M2 31c1-6 5-9 10-9s9 3 10 9"/><rect x="21" y="4" width="11" height="9"/></svg>Live Online Agent Chat Portals</li>
        <li><svg viewBox="0 0 34 34" fill="none" stroke="#fff" stroke-width="1.6"><circle cx="10" cy="20" r="5"/><circle cx="24" cy="20" r="5"/><path d="M17 3v6M10 6l3 4M24 6l-3 4"/></svg>Online Consumer Dispute<br>/Complaint Tools</li>
        <li><svg viewBox="0 0 34 34" fill="none" stroke="#fff" stroke-width="1.6"><rect x="4" y="4" width="26" height="26" rx="3"/><circle cx="17" cy="17" r="6"/><path d="M17 11v12M11 17h12"/></svg>FISMA Compliant Physical and<br>Virtual Security</li>
      </ul>
      <div class="bundle">
        <p class="bundle-title">An Impactful<br>All-In-One<br>Solution</p>
        <ul class="bundle-list" style="left:182px"><li>Credit Report Monitoring</li><li>Address/Phone Scrubbing</li><li>Compliant Collection Letters</li><li>Discretionary Credit Reporting</li><li>Customizable Collection Workflow</li></ul>
        <ul class="bundle-list" style="left:403px"><li>Professional Skip Tracing</li><li>Deceased/Probate Services</li><li>Call Recording and Monitoring</li><li>Bankruptcy Claim Services</li><li>Legal Collection Services</li></ul>
      </div>
      <div class="call" style="top:769px"><p class="call-label">CALL US AT</p><p class="call-number"><svg viewBox="0 0 24 24" fill="currentColor"><path d="M6.6 10.8a15 15 0 006.6 6.6l2.2-2.2c.3-.3.7-.4 1-.2 1.1.4 2.3.6 3.6.6.6 0 1 .4 1 1V20c0 .6-.4 1-1 1A17 17 0 013 4c0-.6.4-1 1-1h3.5c.6 0 1 .4 1 1 0 1.3.2 2.5.6 3.6.1.3 0 .7-.2 1z"/></svg>(555)014-2200</p></div>
      <p class="web" style="top:788px"><svg viewBox="0 0 16 16" fill="none" stroke="#7badd7" stroke-width="1.3"><circle cx="8" cy="8" r="6.5"/><path d="M1.5 8h13M8 1.5c3 3.5 3 9.5 0 13M8 1.5c-3 3.5-3 9.5 0 13"/></svg>www.tririverrecovery.com</p>
    </div>
  </section>

  <section class="slot slot-tr">
    <div class="flyer flyer-philosophy">
      <svg class="shapes" viewBox="0 0 664 860">
        <defs>
          <linearGradient id="philBlue1" x1="0" y1="0" x2="0" y2="1"><stop offset="0" stop-color="#0a86c0"/><stop offset="1" stop-color="#0a4268"/></linearGradient>
          <linearGradient id="headBand1" x1="0" y1="0" x2="1" y2="0"><stop offset="0" stop-color="#2f3438"/><stop offset=".55" stop-color="#3d4449"/><stop offset="1" stop-color="#3d4449" stop-opacity="0"/></linearGradient>
        </defs>
        <path d="M0 380 C90 520 300 560 520 510 C600 490 640 470 664 460 L664 860 L0 860 Z" fill="url(#philBlue1)"/>
        <path d="M575 0 C660 120 650 360 560 450 L600 450 C680 340 690 120 615 0 Z" fill="var(--deep)"/>
        <path d="M540 0 C620 140 620 330 530 430 L560 440 C650 330 650 140 570 0 Z" fill="var(--sky)"/>
        <path d="M0 210 C20 420 220 540 460 490 C380 540 160 560 0 430 Z" fill="var(--slate)"/>
        <path d="M0 140 L600 140 C640 250 600 400 480 460 C330 530 120 480 20 320 L0 280 Z" fill="#c8d6e4" role="img" aria-label="Photo of two business professionals reviewing financial charts at a laptop"/>
        <rect x="0" y="32" width="440" height="108" fill="url(#headBand1)"/>
      </svg>
      <div class="brand" style="top:42px"><span class="brand-dot"></span><span class="brand-name">TRI-RIVER<br>RECOVERY</span></div>
      <div class="philosophy-head"><h2>OUR PHILOSOPHY</h2><span></span></div>
      <p class="philosophy-copy">For over 30 years, Tri-River Recovery has assisted banks and financial services companies in the reconciliation of their past due accounts. Our philosophy is to provide consistent performance by investing in our clients' accounts to ensure the maximum liquidation. By building on historically proven collection techniques and employing an ever-expanding access to data and technology, our agency has continued to improve our performance to the benefit of our clients. Our capital forward, compliance centered approach has proven to deliver the most consistent results for our financial service providers.</p>
      <div class="call" style="top:766px"><p class="call-label">CALL US AT</p><p class="call-number"><svg viewBox="0 0 24 24" fill="currentColor"><path d="M6.6 10.8a15 15 0 006.6 6.6l2.2-2.2c.3-.3.7-.4 1-.2 1.1.4 2.3.6 3.6.6.6 0 1 .4 1 1V20c0 .6-.4 1-1 1A17 17 0 013 4c0-.6.4-1 1-1h3.5c.6 0 1 .4 1 1 0 1.3.2 2.5.6 3.6.1.3 0 .7-.2 1z"/></svg>(555)014-2200</p></div>
      <p class="web" style="top:784px"><svg viewBox="0 0 16 16" fill="none" stroke="#7badd7" stroke-width="1.3"><circle cx="8" cy="8" r="6.5"/><path d="M1.5 8h13M8 1.5c3 3.5 3 9.5 0 13M8 1.5c-3 3.5-3 9.5 0 13"/></svg>www.tririverrecovery.com</p>
    </div>
  </section>

  <section class="slot slot-bl">
    <div class="flyer flyer-services">
      <svg class="shapes" viewBox="0 0 664 860">
        <defs>
          <radialGradient id="medPhoto" cx=".55" cy=".45" r=".6">
            <stop offset="0" stop-color="#f1f3f6"/>
            <stop offset=".7" stop-color="#d9e0e8"/>
            <stop offset="1" stop-color="#a9b7c6"/>
          </radialGradient>
        </defs>
        <path d="M664 30 C500 40 370 140 330 250 C295 340 280 420 290 480 C320 600 460 670 664 665 Z" fill="#0a5f92" opacity=".8"/>
        <path d="M664 50 C520 60 410 140 362 240 C322 320 302 380 304 430 C307 540 402 640 530 650 C590 654 635 648 664 642 Z" fill="var(--white)"/>
        <circle cx="602" cy="388" r="236" fill="url(#medPhoto)" role="img" aria-label="Photo of a smiling female doctor in a white coat with a stethoscope"/>
      </svg>
      <div class="brand"><span class="brand-dot"></span><span class="brand-name">TRI-RIVER<br>RECOVERY</span></div>
      <h1 class="title" style="top:192px"><span class="title-sub" style="line-height:36px">HEALTHCARE</span><span class="title-sub" style="line-height:36px">COLLECTIONS</span></h1>
      <p class="tagline" style="top:293px">A Forward<br>Thinking Approach</p>
      <ul class="features" style="top:354px">
        <li style="height:52px"><svg viewBox="0 0 34 34" fill="none" stroke="#fff" stroke-width="1.6"><circle cx="10" cy="9" r="4"/><path d="M3 30v-9c0-3 3-5 7-5M16 30l6-14 8 2"/></svg>A Patient Friendly,<br>Professional Approach</li>
        <li style="height:52px"><svg viewBox="0 0 34 34" fill="none" stroke="#fff" stroke-width="1.6"><circle cx="11" cy="12" r="6"/><path d="M2 31c1-6 5-9 9-9s8 3 9 9"/><rect x="20" y="4" width="12" height="10"/></svg>Live, Online Agent<br>Chat Portal</li>
        <li style="height:52px"><svg viewBox="0 0 34 34" fill="none" stroke="#fff" stroke-width="1.6"><rect x="3" y="4" width="10" height="9"/><rect x="21" y="4" width="10" height="9"/><path d="M5 24l7-5 5 4 5-4 7 5-6 6h-12z"/></svg>Online Debt<br>Negotiating Tools</li>
        <li style="height:52px"><svg viewBox="0 0 34 34" fill="none" stroke="#fff" stroke-width="1.6"><rect x="7" y="3" width="20" height="26"/><path d="M11 10h12M11 16h12M11 22h7"/></svg>Online Dispute<br>Resolution Tools</li>
        <li style="height:52px"><svg viewBox="0 0 34 34" fill="none" stroke="#fff" stroke-width="1.6"><rect x="4" y="3" width="22" height="28"/><path d="M8 10h14M8 16h10"/><circle cx="24" cy="24" r="6"/></svg>501(r) Compliant</li>
      </ul>
      <div class="bundle">
        <p class="bundle-title">An Impactful<br>All-In-One<br>Solution</p>
        <ul class="bundle-list" style="left:175px"><li>Credit Report Monitoring</li><li>Address/Phone Scrubbing</li><li>Compliant Collection Letters</li><li>Discretionary Credit Reporting</li><li>Bankruptcy Claim Services</li></ul>
        <ul class="bundle-list" style="left:382px"><li>Professional Skip Tracing</li><li>Deceased/Probater Services</li><li>Call Recording and Monitoring</li><li>Legal Collection Services</li><li>Customizable Collection Workflow</li></ul>
      </div>
      <div class="call" style="top:769px"><p class="call-label">CALL US AT</p><p class="call-number"><svg viewBox="0 0 24 24" fill="currentColor"><path d="M6.6 10.8a15 15 0 006.6 6.6l2.2-2.2c.3-.3.7-.4 1-.2 1.1.4 2.3.6 3.6.6.6 0 1 .4 1 1V20c0 .6-.4 1-1 1A17 17 0 013 4c0-.6.4-1 1-1h3.5c.6 0 1 .4 1 1 0 1.3.2 2.5.6 3.6.1.3 0 .7-.2 1z"/></svg>(555)014-2200</p></div>
      <p class="web" style="top:786px"><svg viewBox="0 0 16 16" fill="none" stroke="#7badd7" stroke-width="1.3"><circle cx="8" cy="8" r="6.5"/><path d="M1.5 8h13M8 1.5c3 3.5 3 9.5 0 13M8 1.5c-3 3.5-3 9.5 0 13"/></svg>www.tririverrecovery.com</p>
    </div>
  </section>

  <section class="slot slot-br">
    <div class="flyer flyer-philosophy">
      <svg class="shapes" viewBox="0 0 664 860">
        <defs>
          <linearGradient id="philBlue2" x1="0" y1="0" x2="0" y2="1"><stop offset="0" stop-color="#0a86c0"/><stop offset="1" stop-color="#0a4268"/></linearGradient>
          <linearGradient id="headBand2" x1="0" y1="0" x2="1" y2="0"><stop offset="0" stop-color="#2f3438"/><stop offset=".55" stop-color="#3d4449"/><stop offset="1" stop-color="#3d4449" stop-opacity="0"/></linearGradient>
        </defs>
        <path d="M0 380 C90 520 300 560 520 510 C600 490 640 470 664 460 L664 860 L0 860 Z" fill="url(#philBlue2)"/>
        <path d="M575 0 C660 120 650 360 560 450 L600 450 C680 340 690 120 615 0 Z" fill="var(--deep)"/>
        <path d="M540 0 C620 140 620 330 530 430 L560 440 C650 330 650 140 570 0 Z" fill="var(--sky)"/>
        <path d="M0 210 C20 420 220 540 460 490 C380 540 160 560 0 430 Z" fill="var(--slate)"/>
        <path d="M0 140 L600 140 C640 250 600 400 480 460 C330 530 120 480 20 320 L0 280 Z" fill="#b9d3e6" role="img" aria-label="Photo of a team of doctors and nurses gathered around a glass table with a laptop"/>
        <rect x="0" y="32" width="440" height="108" fill="url(#headBand2)"/>
      </svg>
      <div class="brand" style="top:42px"><span class="brand-dot"></span><span class="brand-name">TRI-RIVER<br>RECOVERY</span></div>
      <div class="philosophy-head"><h2>OUR PHILOSOPHY</h2><span></span></div>
      <p class="philosophy-copy" style="line-height:20px">Since our inception, and for over 40 years, healthcare collections have been at the center of our operation. Our philosophy is to provide consistent performance by investing in our clients accounts to ensure the maximum liquidation. By building on historically proven collection techniques and employing an ever-expanding access to data and technology, our agency has continued to improve our performance to the benefit of our clients. Our capital forward, compliance centered approach has proven to deliver consistent results to our healthcare providers.</p>
      <div class="call" style="top:766px"><p class="call-label">CALL US AT</p><p class="call-number"><svg viewBox="0 0 24 24" fill="currentColor"><path d="M6.6 10.8a15 15 0 006.6 6.6l2.2-2.2c.3-.3.7-.4 1-.2 1.1.4 2.3.6 3.6.6.6 0 1 .4 1 1V20c0 .6-.4 1-1 1A17 17 0 013 4c0-.6.4-1 1-1h3.5c.6 0 1 .4 1 1 0 1.3.2 2.5.6 3.6.1.3 0 .7-.2 1z"/></svg>(555)014-2200</p></div>
      <p class="web" style="top:782px"><svg viewBox="0 0 16 16" fill="none" stroke="#7badd7" stroke-width="1.3"><circle cx="8" cy="8" r="6.5"/><path d="M1.5 8h13M8 1.5c3 3.5 3 9.5 0 13M8 1.5c-3 3.5-3 9.5 0 13"/></svg>www.tririverrecovery.com</p>
    </div>
  </section>

</main>
</body>
</html>
```